Business Card Design Project

Professional business cards for law firm - a rough example of what we are looking for is attached. The logo, colour and styling of the name are all new and dont need to be changed. We need layout for front and back. We are looking for some imaginative layout of info. We are a young vibrant firm and not too conservative and are not adverse to something quite different.
Updates

Thank you for all the submissions.  We have been blown away with the quality of your work.  Our management team will be meeting later in the week to make our decision.  Again, thanks for the fabulous work.

Industry/Entity Type

Conservative

Requirements
Must have
• Logo and name as in attached example (colour and font)
Should not have
• Scales of Justice

```html
<!DOCTYPE html>
<html lang="en">
<head>
<meta charset="utf-8">
<title>Marsh Vale Legal – Round Business Card</title>
<link href="https://fonts.googleapis.com/css2?family=Noto+Sans:wght@400&family=Arimo:wght@400&display=swap" rel="stylesheet">
<style>
  :root {
    --page: #ffffff;
    --front-top: #3b5370;
    --front-mid: #8496ab;
    --front-bottom: #eceef1;
    --back-top: #585d68;
    --back-bottom: #f2f2f4;
    --brand-green: #2f5418;
    --brand-green-light: #4e7a2c;
    --ink-navy: #14294a;
    --services: #ffffff;
    --disc: #aab7c6;
  }
  html, body {
    margin: 0;
    width: 1200px;
    height: 1200px;
    overflow: hidden;
    background: var(--page);
  }
  .canvas {
    position: relative;
    width: 1200px;
    height: 1200px;
  }
  .card {
    position: absolute;
    width: 416px;
    height: 416px;
    border-radius: 50%;
    overflow: hidden;
    box-shadow: 0 10px 22px rgba(0,0,0,0.28);
  }
  .card-back {
    left: 577px;
    top: 407px;
    background: linear-gradient(to bottom, var(--back-top), #8d8f96 50%, var(--back-bottom));
    z-index: 1;
  }
  .card-front {
    left: 239px;
    top: 407px;
    background: linear-gradient(to bottom, var(--front-top), var(--front-mid) 50%, var(--front-bottom));
    z-index: 2;
  }
  .brand-disc {
    position: absolute;
    left: 108px;
    top: 108px;
    width: 200px;
    height: 200px;
    border-radius: 50%;
    background: var(--disc);
  }
  .brand-initials {
    position: absolute;
    left: 0;
    width: 416px;
    top: 172px;
    text-align: center;
    font-family: "Noto Sans", sans-serif;
    font-size: 62px;
    line-height: 72px;
    color: var(--brand-green);
  }
  .services {
    position: absolute;
    left: 0;
    width: 446px;
    text-align: center;
    font-family: "Arimo", sans-serif;
    font-size: 12px;
    color: var(--services);
    white-space: nowrap;
    margin: 0;
  }
  .services-1 { top: 100px; }
  .services-2 { top: 119px; }
  .firm-name {
    position: absolute;
    left: 0;
    width: 416px;
    top: 152px;
    text-align: center;
    font-family: "Noto Sans", sans-serif;
    font-size: 33px;
    line-height: 40px;
    color: var(--brand-green-light);
    margin: 0;
    font-weight: 400;
  }
  .firm-tag {
    position: absolute;
    left: 0;
    width: 416px;
    top: 194px;
    text-align: center;
    font-family: "Noto Sans", sans-serif;
    font-size: 19px;
    letter-spacing: 2px;
    color: var(--brand-green);
  }
  .contact {
    position: absolute;
    left: 0;
    width: 446px;
    top: 235px;
    text-align: center;
    font-family: "Noto Sans", sans-serif;
    font-size: 16px;
    line-height: 23.5px;
    color: var(--ink-navy);
    font-style: normal;
    white-space: nowrap;
  }
</style>
</head>
<body>
<main class="canvas">
  <section class="card card-back" aria-label="Card back">
    <p class="services services-1">Family &nbsp;.&nbsp; Restraining Orders &nbsp;.&nbsp; Probate/wills &nbsp;.&nbsp; Diving Fences</p>
    <p class="services services-2">Traffic &nbsp;.&nbsp; Criminal &nbsp;.&nbsp; Debt Recovery &nbsp;.&nbsp; Financial Agreements</p>
    <h1 class="firm-name">Marsh Vale</h1>
    <div class="firm-tag">LEGAL</div>
    <address class="contact">
      48 Harbour Street, Eastvale WA 6100<br>
      PO Box 312, Eastvale WA 6980<br>
      T: 9000 1234 . 9000 5678<br>
      F: 9000 4321<br>
      reception@marshvalelegal.com.au
    </address>
  </section>
  <section class="card card-front" aria-label="Card front">
    <div class="brand-disc"></div>
    <div class="brand-initials">MVL</div>
  </section>
</main>
</body>
</html>
```